Brackenmoor.com.au - Quorvel Australia - Uncoded PSD only

We need a web design for a virtual assistant company based in Sydney Australia called "Brackenmoor". We provide virtual assistance and unlimited admin tasks to small business owners for a monthly fee. We would like to see designs that are not too different to www.quorvel.com. Words to describe the design and feel of this website are sleek and professional. We want to use bright inviting colours for the call to action buttons and a professional business focused background.

Target Market(s)

business executives, business owners, small business owners, those professionals who lack time.

Industry/Entity Type

Business Consultant

Number of Pages Required

3 page

Font styles to use
Sans Serif

Colors
5e5e5e
1b1b1b
3176b5
33b8a4

Requirements
Must have
• Call to action buttons, sleek business feel think plovix.io and quorvel.com
Nice to have
• Bold back ground colours, bright call to action buttons
Should not have
• too much white

```html
<!DOCTYPE html>
<html lang="en">
<head>
<meta charset="utf-8">
<title>Brackenmoor — Virtual Assistance</title>
<link rel="stylesheet" href="https://fonts.googleapis.com/css2?family=Open+Sans:wght@400;600;700;800&display=swap">
<style>
:root{
  --blue:#3176b5;
  --blue-dark:#245d92;
  --teal:#33b8a4;
  --ink:#1b1b1b;
  --grey:#5e5e5e;
  --light:#f2f3f5;
  --line:#dcdfe3;
  --footer:#1e1f22;
  --footer-deep:#141517;
  --white:#ffffff;
}
*{box-sizing:border-box;margin:0;padding:0}
html,body{width:1200px;height:2800px;overflow:hidden}
body{font-family:"Open Sans",Arial,sans-serif;color:var(--grey);background:var(--white);font-size:14px;line-height:1.6}
.wrap{width:1000px;margin:0 auto;position:relative}
a{color:inherit;text-decoration:none}

/* header */
.site-header{height:70px;background:var(--white);border-bottom:1px solid var(--line)}
.site-header .wrap{display:flex;align-items:center;height:70px}
.brand{font-size:28px;font-weight:800;color:var(--blue);letter-spacing:1px;text-transform:uppercase}
.header-right{margin-left:auto;display:flex;flex-direction:column;align-items:flex-end;gap:4px}
.topline{font-size:11px;color:var(--grey);display:flex;gap:16px}
.main-nav{display:flex;align-items:center;gap:0}
.main-nav a{font-size:14px;color:var(--ink);padding:4px 14px;border-right:1px solid var(--line)}
.main-nav a:last-of-type{border-right:none}
.search{width:26px;height:26px;border-radius:50%;border:1px solid var(--line);display:flex;align-items:center;justify-content:center;margin-left:8px}

/* hero */
.hero{height:450px;position:relative;overflow:hidden}
.hero-photo{position:absolute;inset:0;background:linear-gradient(180deg,#8a9198 0%,#4c545d 45%,#2c3238 100%)}
.hero-content{position:relative;text-align:center;color:var(--white);padding-top:140px}
.hero h1{font-size:44px;font-weight:700;margin-bottom:14px}
.hero p{font-size:15px;width:820px;margin:0 auto 42px}
.btn{display:inline-block;padding:11px 32px;font-size:14px;font-weight:600;color:var(--white);border-radius:2px}
.btn-teal{background:var(--teal)}
.btn-blue{background:var(--blue)}
.hero .btn{margin:0 8px}
.hero-arrow{position:absolute;top:210px;width:34px;height:34px;border:2px solid rgba(255,255,255,.7);border-radius:50%}
.hero-arrow.left{left:130px}.hero-arrow.right{right:130px}

/* what we do */
.what{height:480px;overflow:hidden}
.what .wrap{display:flex;height:480px}
.what-photo{width:300px;height:440px;margin-top:40px;background:linear-gradient(180deg,#e9e9eb 0%,#3a3a3e 100%);border-radius:2px}
.what-body{flex:1;padding:60px 0 0 60px}
.section-title{font-size:28px;font-weight:700;color:var(--ink);text-transform:uppercase;margin-bottom:12px}
.what-body .intro{font-size:13px;margin-bottom:26px}
.services{display:grid;grid-template-columns:1fr 1fr;gap:22px 40px;margin-bottom:34px}
.service{display:flex;gap:14px}
.service svg{flex:none}
.service h3{font-size:15px;font-weight:700;color:var(--ink)}
.service p{font-size:12px;line-height:1.5}

/* call band */
.call-band{height:260px;background:var(--blue);color:var(--white);text-align:center;padding-top:50px}
.call-band h2{font-size:30px;font-weight:700}
.call-band p{font-size:16px;margin-top:4px}
.call-icons{display:flex;justify-content:center;gap:40px;margin-top:34px}
.call-icons span{width:62px;height:62px;border:2px solid var(--white);border-radius:50%;display:flex;align-items:center;justify-content:center}

/* who we are */
.who{height:340px;position:relative;background:var(--light);overflow:hidden}
.who-photo{position:absolute;right:0;top:0;width:660px;height:340px;background:linear-gradient(90deg,var(--light) 0%,#a9b3bd 35%,#3b4148 100%)}
.who-body{position:relative;width:500px;padding-top:40px}
.who-body p{font-size:13px;margin-bottom:14px}

/* blog */
.blog{height:400px;text-align:center;padding-top:44px}
.posts{display:grid;grid-template-columns:repeat(3,1fr);gap:36px;margin-top:22px}
.post-photo{height:180px;background:linear-gradient(160deg,#d9dde2 0%,#7b8591 100%)}
.post h3{font-size:14px;font-weight:700;color:var(--ink);margin-top:14px;text-transform:uppercase}
.post p{font-size:12px;padding:0 20px}

/* news & testimonials */
.lower{height:380px;background:var(--light);padding-top:40px}
.lower .wrap{display:flex;gap:60px}
.col-title{font-size:22px;font-weight:700;color:var(--ink);margin-bottom:18px}
.news{width:440px}
.news-item{display:flex;gap:16px;margin-bottom:18px}
.news-date{width:58px;height:58px;background:var(--blue);color:var(--white);text-align:center;font-size:12px;line-height:1.3;padding-top:10px;flex:none}
.news-date b{display:block;font-size:18px}
.news-item h4{font-size:14px;font-weight:600;color:var(--ink)}
.news-item p{font-size:12px}
.testimonials{flex:1}
.testimonials .head{display:flex;align-items:center}
.pager{margin-left:auto;display:flex;gap:3px}
.pager span{width:20px;height:20px;background:var(--blue)}
.quote{background:var(--white);border:1px solid var(--line);padding:22px;display:flex;gap:20px}
.avatar{width:90px;height:90px;border-radius:50%;background:linear-gradient(160deg,#c9b7a8,#6b5f58);flex:none}
.quote p{font-size:13px}
.quote-name{color:var(--blue);font-weight:700;margin-top:12px}

/* footer */
.site-footer{height:380px;background:var(--footer);color:#a9adb2;padding-top:44px}
.site-footer .wrap{display:grid;grid-template-columns:1.3fr 1fr 1.2fr 1.1fr;gap:40px}
.site-footer h5{color:var(--white);font-size:15px;font-weight:600;margin-bottom:16px}
.site-footer p,.site-footer li{font-size:12px}
.site-footer ul{list-style:none}
.site-footer li{margin-bottom:8px;padding-left:12px;position:relative}
.site-footer li::before{content:"";position:absolute;left:0;top:7px;width:4px;height:4px;background:var(--teal)}
.contact-row{display:flex;gap:10px;margin-bottom:12px;font-size:12px;align-items:center}
.contact-row i{width:24px;height:24px;border-radius:50%;background:var(--blue);flex:none}
.field{height:32px;background:#2d2f33;border:1px solid #3a3c40;margin:10px 0;padding:6px 10px;font-size:12px}
.subscribe{background:var(--blue);color:var(--white);font-size:12px;padding:6px 18px;display:inline-block}
.copyright{height:40px;background:var(--footer-deep);color:#8d9196;font-size:12px}
.copyright .wrap{display:flex;align-items:center;height:40px}
.socials{margin-left:auto;display:flex;gap:6px}
.socials span{width:22px;height:22px;border-radius:50%;background:var(--blue)}
</style>
</head>
<body>
<header class="site-header">
  <div class="wrap">
    <a class="brand" href="#">Brackenmoor</a>
    <div class="header-right">
      <div class="topline"><span>0190 555 0148</span><span>hello@brackenmoor.com.au</span></div>
      <nav class="main-nav">
        <a href="#">Home</a><a href="#">About Us</a><a href="#">Service</a><a href="#">Testimonial</a><a href="#">Contact Us</a>
        <span class="search"><svg width="12" height="12" viewBox="0 0 12 12"><circle cx="5" cy="5" r="3.5" fill="none" stroke="#5e5e5e" stroke-width="1.5"/><line x1="7.6" y1="7.6" x2="11" y2="11" stroke="#5e5e5e" stroke-width="1.5"/></svg></span>
      </nav>
    </div>
  </div>
</header>

<section class="hero">
  <div class="hero-photo" role="img" aria-label="Business team meeting silhouetted against an office window"></div>
  <span class="hero-arrow left"></span><span class="hero-arrow right"></span>
  <div class="hero-content">
    <h1>Welcome To BRACKENMOOR</h1>
    <p>Lorem ipsum dolor sit amet, consectetur adipiscing elit. Pellentesque tempus nisi at facilisis porta. Vivamus a est et nisi. Suspendisse.</p>
    <a class="btn btn-teal" href="#">Learn More</a><a class="btn btn-blue" href="#">Request A Consultation</a>
  </div>
</section>

<section class="what">
  <div class="wrap">
    <div class="what-photo" role="img" aria-label="Smiling businesswoman in a dark suit with arms crossed"></div>
    <div class="what-body">
      <h2 class="section-title">What We Do</h2>
      <p class="intro">Lorem ipsum dolor sit amet, consectetur adipiscing elit. Pellentesque tempus nisi at facilisis porta. Vivamus a est et nisi. Suspendisse consectetur lorem ultrices, mollis ligula nec, commodo libero. Quisque porttitor augue arcu, at tristique sapien aliquam nec. Aliquam massa purus, mollis vel arcu et, sodales sollicitudin ante.</p>
      <div class="services">
        <div class="service"><svg width="40" height="40" viewBox="0 0 40 40"><circle cx="20" cy="14" r="7" fill="#3176b5"/><path d="M6 36c0-8 6-13 14-13s14 5 14 13z" fill="#3176b5"/></svg><div><h3>Lorem ipsum dolor sit</h3><p>Consectetur adipiscing elit. Nullam tempus finibus nisi.</p></div></div>
        <div class="service"><svg width="40" height="40" viewBox="0 0 40 40"><circle cx="20" cy="14" r="7" fill="#3176b5"/><path d="M6 36c0-8 6-13 14-13s14 5 14 13z" fill="#3176b5"/></svg><div><h3>Lorem ipsum dolor sit</h3><p>Consectetur adipiscing elit. Nullam tempus finibus nisi.</p></div></div>
        <div class="service"><svg width="40" height="40" viewBox="0 0 40 40"><circle cx="20" cy="14" r="7" fill="#3176b5"/><path d="M6 36c0-8 6-13 14-13s14 5 14 13z" fill="#3176b5"/></svg><div><h3>Lorem ipsum dolor sit</h3><p>Consectetur adipiscing elit. Nullam tempus finibus nisi.</p></div></div>
        <div class="service"><svg width="40" height="40" viewBox="0 0 40 40"><circle cx="20" cy="14" r="7" fill="#3176b5"/><path d="M6 36c0-8 6-13 14-13s14 5 14 13z" fill="#3176b5"/></svg><div><h3>Lorem ipsum dolor sit</h3><p>Consectetur adipiscing elit. Nullam tempus finibus nisi.</p></div></div>
      </div>
      <a class="btn btn-teal" href="#">Read more</a>
    </div>
  </div>
</section>

<section class="call-band">
  <h2>Are you having any problems but can't consult to anyone?</h2>
  <p>Talk to us! We promise we can help you! Call Now! 0190 555 0148</p>
  <div class="call-icons">
    <span><svg width="26" height="26" viewBox="0 0 24 24"><path d="M6.6 10.8a15 15 0 006.6 6.6l2.2-2.2c.3-.3.7-.4 1-.2 1.1.4 2.3.6 3.6.6.6 0 1 .4 1 1V20c0 .6-.4 1-1 1A17 17 0 013 4c0-.6.4-1 1-1h3.5c.6 0 1 .4 1 1 0 1.3.2 2.5.6 3.6.1.3 0 .7-.2 1z" fill="#fff"/></svg></span>
    <span><svg width="26" height="26" viewBox="0 0 24 24"><path d="M4 4h16v11H8l-4 4z" fill="#fff"/></svg></span>
  </div>
</section>

<section class="who">
  <div class="who-photo" role="img" aria-label="Businessman in a suit adjusting his jacket"></div>
  <div class="wrap">
    <div class="who-body">
      <h2 class="section-title">Who We Are</h2>
      <p>Lorem ipsum dolor sit amet, consectetur adipiscing elit. Pellentesque tempus nisi at facilisis porta. Vivamus a est et nisi. Suspendisse consectetur lorem ultrices, mollis ligula nec, commodo libero. Quisque porttitor augue arcu, at tristique sapien aliquam nec. Aliquam massa purus, mollis vel arcu et, sodales sollicitudin ante.</p>
      <p>Quisque porttitor augue arcu, at tristique sapien aliquam nec. Aliquam massa purus, mollis vel arcu et, sodales sollicitudin ante. Consectetur lorem ultrices, mollis ligula nec, commodo libero.</p>
      <a class="btn btn-blue" href="#">Read More</a>
    </div>
  </div>
</section>

<section class="blog">
  <div class="wrap">
    <h2 class="section-title">Our Blog</h2>
    <div class="posts">
      <article class="post"><div class="post-photo" role="img" aria-label="Two colleagues reviewing work at a laptop"></div><h3>Lorem ipsum dolor sit ame</h3><p>Lorem ipsum dolor sit amet, consectetur adipiscing elit. Ut vitae aliquam.</p></article>
      <article class="post"><div class="post-photo" role="img" aria-label="Team discussing documents around a meeting table"></div><h3>Lorem ipsum dolor sit ame</h3><p>Lorem ipsum dolor sit amet, consectetur adipiscing elit. Ut vitae aliquam.</p></article>
      <article class="post"><div class="post-photo" role="img" aria-label="Business group seated together in a bright office"></div><h3>Lorem ipsum dolor sit ame</h3><p>Lorem ipsum dolor sit amet, consectetur adipiscing elit. Ut vitae aliquam.</p></article>
    </div>
  </div>
</section>

<section class="lower">
  <div class="wrap">
    <div class="news">
      <h2 class="col-title">Latest News</h2>
      <div class="news-item"><div class="news-date"><b>21</b>Mar</div><div><h4>Lorem ipsum dolor sit amet, consectetur</h4><p>Adipiscing elit. Nullam tempus finibus nisi sed porttitor.</p></div></div>
      <div class="news-item"><div class="news-date"><b>21</b>Mar</div><div><h4>Lorem ipsum dolor sit amet, consectetur</h4><p>Adipiscing elit. Nullam tempus finibus nisi sed porttitor.</p></div></div>
      <div class="news-item"><div class="news-date"><b>21</b>Mar</div><div><h4>Lorem ipsum dolor sit amet, consectetur</h4><p>Adipiscing elit. Nullam tempus finibus nisi sed porttitor.</p></div></div>
    </div>
    <div class="testimonials">
      <div class="head"><h2 class="col-title">Our Testimonials</h2><div class="pager"><span></span><span></span></div></div>
      <div class="quote">
        <div class="avatar" role="img" aria-label="Portrait of a client"></div>
        <div><p>Lorem ipsum dolor sit amet, consectetur adipiscing elit. Nullam tempus finibus nisi, sed porttitor augue. Quisque porttitor augue arcu, at tristique sapien aliquam nec. Aliquam massa purus, mollis vel arcu.</p>
        <div class="quote-name">Lorem Ipsum</div></div>
      </div>
    </div>
  </div>
</section>

<footer class="site-footer">
  <div class="wrap">
    <div><h5>About us</h5><p>We provide our customers with the best virtual assistance possible. We aim to be excellent at delivering admin tasks for small business owners and busy professionals across Sydney and Australia.</p></div>
    <div><h5>Main menu</h5><ul><li>Home</li><li>About Us</li><li>Service</li><li>Testimonial</li><li>Contact Us</li></ul></div>
    <div><h5>Contact us</h5>
      <div class="contact-row"><i></i>Lorem ipsum dolor sit amet, Sydney NSW</div>
      <div class="contact-row"><i></i>0190 555 0148</div>
      <div class="contact-row"><i></i>hello@brackenmoor.com.au</div>
    </div>
    <div><h5>Newsletter</h5><div class="field">Name</div><div class="field">Email</div><span class="subscribe">Submit</span></div>
  </div>
</footer>
<div class="copyright">
  <div class="wrap"><span>Copyright © 2015 Brackenmoor.com.au</span><div class="socials"><span></span><span></span><span></span><span></span></div></div>
</div>
</body>
</html>
```